Flyer-Design für Hochzeitswebseiten
Zielgruppe
Wir machen Hochzeitswebseiten ( www.holdtheday-web.de).
Aufgabenstellung
Gerne hätte ich folgendes DIN Format: 210x148 quer mit 6 Seiten. 1 Seite schwarz mit unserem Logo. 2 Seite Bild. 3 Seite Text. 4 Seite 4-5 Bilder. 5 Seite Text. 6 Seite Kontaktinformationen.
Text1:
Ihr habt alles dafür getan, dass Eure Hochzeit so schön wie möglich wird. Wir tun alles dafür, dass die Erinnerung daran so großartig wie möglich bleibt. Ihr stellt uns Eure persönlichen Informationen und Fotos zur Verfügung. Wir machen daraus eine professionelle Website über den schönsten Tag Eures Lebens. Ihr entscheidet über Umfang und Budget.
Wir widmen uns jedem Auftrag mit Begeisterung und Kreativität.
Text2: evtl. sollte da das Basic und Premiumpaket beschrieben werden. Sind uns da aber unsicher.

```html
<!DOCTYPE html>
<html lang="de">
<head>
<meta charset="utf-8">
<title>Hold the Day – Flyer Titel und Bildseite</title>
<link rel="stylesheet" href="https://fonts.googleapis.com/css2?family=Cinzel:wght@400&display=swap">
<style>
  :root {
    --bg: #b9d0cf;
    --cover-black: #1b1b1b;
    --cover-black-light: #333333;
    --gold: #d4b25a;
    --gold-line: #c9a54b;
    --wood-dark: #5d5853;
    --wood-mid: #7a746d;
    --wood-light: #948d85;
    --rose: #c9264d;
    --rose-soft: rgba(201, 38, 77, 0.55);
    --photo-dark: #4a4d4c;
    --photo-green: #8c9870;
    --photo-light: #dcd8cf;
  }
  * { margin: 0; padding: 0; box-sizing: border-box; }
  html, body { width: 1200px; height: 720px; overflow: hidden; }
  body {
    background: var(--bg);
    display: flex;
    align-items: center;
    justify-content: center;
  }
  .spread {
    display: flex;
    width: 1120px;
    height: 394px;
    box-shadow: 0 14px 36px rgba(40, 70, 70, 0.25);
  }
  .page { position: relative; width: 560px; height: 394px; overflow: hidden; }

  /* Titelseite */
  .cover {
    background: radial-gradient(ellipse at 65% 25%, var(--cover-black-light), var(--cover-black) 75%);
  }
  .brand-name {
    position: absolute;
    left: 0; right: 0; top: 168px;
    text-align: center;
    font-family: "Cinzel", serif;
    font-weight: 400;
    font-size: 48px;
    line-height: 1;
    letter-spacing: 3px;
    color: var(--gold);
  }

  /* Bildseite */
  .picture-page {
    background:
      radial-gradient(ellipse 190px 160px at 110px 300px, var(--rose) 0%, var(--rose-soft) 45%, rgba(201, 38, 77, 0) 100%),
      radial-gradient(ellipse 120px 80px at 40px 120px, rgba(170, 40, 70, 0.45) 0%, rgba(170, 40, 70, 0) 100%),
      linear-gradient(160deg, var(--wood-light) 0%, var(--wood-mid) 40%, var(--wood-dark) 70%, var(--wood-mid) 100%);
  }
  .inset-photo {
    position: absolute;
    left: 175px; top: 70px;
    width: 330px; height: 200px;
    background:
      radial-gradient(ellipse 120px 70px at 230px 60px, var(--photo-light) 0%, rgba(220, 216, 207, 0) 100%),
      linear-gradient(120deg, var(--photo-dark) 0%, var(--photo-green) 45%, #b8b3a6 75%, var(--photo-light) 100%);
    box-shadow: 0 6px 14px rgba(0, 0, 0, 0.35);
  }
  .inset-frame {
    position: absolute;
    left: 175px; top: 70px;
    width: 330px; height: 200px;
    pointer-events: none;
  }
</style>
</head>
<body>
  <main class="spread">
    <section class="page cover" aria-label="Titelseite">
      <h1 class="brand-name">Hold the Day</h1>
    </section>

    <section class="page picture-page" role="img" aria-label="Foto: rote Rose auf einem grauen Holztisch">
      <div class="inset-photo" role="img" aria-label="Foto: Brautpaar hält sich an den Händen, Ehering am Finger, Brautstrauß im Hintergrund"></div>
      <svg class="inset-frame" viewBox="0 0 330 200" aria-hidden="true">
        <rect x="16" y="14" width="298" height="172" fill="none" stroke="var(--gold-line)" stroke-width="1"/>
        <rect x="22" y="20" width="286" height="160" fill="none" stroke="var(--gold-line)" stroke-width="0.8" stroke-dasharray="2 2"/>
      </svg>
    </section>
  </main>
</body>
</html>
```